International IT and cyber security consulting company is looking to establish a web presence.

Halvern Ridge Advisory LLC provides IT, cyber security, risk, project management and data analytics consulting services worldwide. Our clients are both government and corporate. We are looking to establish a basic web presence with about 6 pages (Home, About Halvern, Our Experts, News and Events, Careers, Contact Us). The designs should set the look and feel of the site for further build out down the line. The final design should be straightforward and simple and allow us to convey information about our consulting services clearly.

Target Market(s)

Government and corporate clients or potential clients, job seekers.

Industry/Entity Type

Consulting

Contact Information for Business Card

The cards will have english on the front and arabic on the back. The design should be the same on both sides.

Coding

Number of Pages Required

Font styles to use
Serif
Sans Serif

Requirements
Must have
• The pages should be simple but visually appealing with a picture or graphic that is appropriate to the company or services we offer. Our name and logo should be branded throughout the design. While we are mostly an IT company we also have a line of business where we organize speaking events for VIPs so the website shouldn't overly emphasize our IT work.
Should not have
• No cartoons or drawings. The site should not have overly flashy or loud colors. We cater to a conservative set of clients so the site should match what they expect to see in an international consultancy's website. There should not be an overuse of the color orange because it can be hard on the eyes if it is used too much on the page. Also, please do not use graphics or pictures that use locks, keys, castles, shields etc since these are too commonly used in the cyber security industry.

```html
<!DOCTYPE html>
<html lang="en">
<head>
<meta charset="utf-8">
<title>Halvern Ridge Advisory LLC</title>
<link href="https://fonts.googleapis.com/css2?family=Cinzel:wght@400;500;600&family=Poppins:wght@300;400;500;600&display=swap" rel="stylesheet">
<style>
:root{
  --orange:#f07c1b;
  --orange-deep:#e0620f;
  --ink:#222;
  --text:#444;
  --muted:#777;
  --light:#efefef;
  --white:#fff;
  --night:#06121b;
  --footer:#151515;
}
*{box-sizing:border-box;margin:0;padding:0}
html,body{width:1200px;height:4563px;overflow:hidden}
body{position:relative;background:var(--white);font-family:"Poppins",sans-serif;color:var(--text)}
.abs{position:absolute}
.serif{font-family:"Cinzel",serif}

/* header */
.site-header{position:absolute;left:0;top:0;width:1200px;height:98px;background:var(--white);z-index:3}
.brand{position:absolute;left:52px;top:0;width:310px;height:112px;background:var(--white);border-radius:0 0 28px 28px;display:flex;align-items:center;gap:12px;padding-left:28px;z-index:4}
.brand-mark{width:16px;height:16px;background:var(--orange)}
.brand-name{font-family:"Cinzel",serif;font-size:21px;line-height:1.15;color:var(--orange);font-weight:500;width:220px}
.nav{position:absolute;top:58px;left:475px;display:flex;gap:0;font-size:16px;color:var(--ink)}
.nav a{color:var(--ink);text-decoration:none;margin-right:34px;padding-bottom:10px}
.nav a.active{color:var(--orange);border-bottom:2px solid var(--orange)}
.phone{position:absolute;right:65px;top:14px;display:flex;align-items:center;gap:8px;font-size:16px;color:var(--ink)}
.phone-ic{width:28px;height:28px;border-radius:50%;background:var(--orange);display:flex;align-items:center;justify-content:center}

/* hero */
.hero{position:absolute;left:0;top:98px;width:1200px;height:720px;overflow:hidden}
.hero-art{position:absolute;inset:0;background:
 radial-gradient(ellipse 420px 260px at 820px 500px,#ffb05a 0%,#f07c1b 30%,rgba(160,50,5,.7) 60%,rgba(0,0,0,0) 100%),
 radial-gradient(ellipse 300px 420px at 800px 150px,rgba(240,110,20,.6),rgba(0,0,0,0) 70%),
 linear-gradient(90deg,#050505 0%,#1a0c04 45%,#3a1806 75%,#1b0b03 100%)}
.hero-curve{position:absolute;left:-200px;top:655px;width:1600px;height:300px;border-radius:50%;background:var(--white)}
.hero-kicker{left:135px;top:272px;font-size:21px;color:var(--white);letter-spacing:.5px}
.hero-title{left:131px;top:306px;font-size:41px;line-height:45px;color:var(--white);font-weight:500}
.hero-copy{left:131px;top:428px;width:440px;font-size:14.5px;line-height:24px;color:#eee}
.btn-solid{display:flex;align-items:center;justify-content:center;gap:12px;background:var(--orange);color:var(--white);border-radius:30px;font-size:18px}
.hero-btn{left:131px;top:527px;width:206px;height:48px}
.circ-ic{width:22px;height:22px;border:2px solid currentColor;border-radius:50%;display:inline-flex;align-items:center;justify-content:center}
.arrow-btn{width:46px;height:46px;border-radius:50%;display:flex;align-items:center;justify-content:center}
.arrow-outline{border:2px solid #fff;background:rgba(0,0,0,.15)}
.arrow-fill{background:var(--orange)}

/* welcome */
.welcome-art{left:80px;top:839px;width:460px;height:460px;border-radius:50%;background:radial-gradient(circle at 50% 50%,#f6f6f6 0%,#e6e6e6 70%,#d8d8d8 100%)}
.welcome-node{left:205px;top:945px;width:200px;height:200px;border-radius:50%;background:radial-gradient(circle at 45% 45%,#f39a4a,#c9520c 55%,rgba(60,20,5,.0) 75%)}
.kicker-dark{left:643px;top:912px;font-size:25px;color:var(--ink)}
.welcome-title{left:643px;top:950px;font-size:39px;color:var(--ink);font-weight:500}
.welcome-copy{left:643px;top:1016px;width:440px;font-size:14px;line-height:22px;color:var(--text)}
.btn-outline{display:flex;align-items:center;justify-content:center;gap:12px;border:2px solid var(--orange);color:var(--orange);border-radius:30px;background:var(--white)}
.welcome-btn{left:642px;top:1160px;width:203px;height:53px;font-size:18px}

/* services */
.services{left:0;top:1365px;width:1200px;height:1000px;background:var(--light)}
.section-title{width:1200px;left:0;text-align:center;font-size:42px;color:var(--ink);font-weight:500}
.service-card{position:absolute;width:296px;height:254px;background:var(--white);box-shadow:0 4px 14px rgba(0,0,0,.08);display:flex;flex-direction:column;align-items:center;padding-top:38px}
.service-card svg{width:104px;height:104px}
.service-card .label{margin-top:28px;font-size:20px;font-weight:500;color:var(--ink)}
.service-card.featured{background:linear-gradient(135deg,#f28a2c,#e7641a)}
.service-card.featured .label{color:var(--white)}

/* experts + why */
.dark-band{left:0;top:2190px;width:1200px;height:1015px}
.experts-title{left:167px;top:2438px;font-size:45px;color:var(--white);font-weight:500}
.experts-copy{left:165px;top:2502px;width:350px;font-size:14px;line-height:27px;color:#e4e4e4}
.arrow-sm{width:32px;height:32px;border-radius:50%;display:flex;align-items:center;justify-content:center}
.expert-card{position:absolute;top:2370px;width:176px;height:345px;border-radius:88px;background:var(--white);display:flex;flex-direction:column;align-items:center;padding-top:15px}
.expert-photo{width:150px;height:150px;border-radius:50%;background:linear-gradient(160deg,#c9ced3,#7b838c)}
.expert-name{margin-top:18px;font-size:16px;color:var(--ink)}
.expert-role{font-size:11px;color:var(--muted);text-align:center;line-height:15px;margin-top:4px;min-height:30px}
.social-dot{width:32px;height:32px;border-radius:50%;background:#1f5fbf;margin-top:14px}
.why-title{top:2778px;color:var(--white)}
.why-item{position:absolute;top:2885px;width:260px;margin-left:-130px;text-align:center;color:var(--white)}
.why-ic{width:96px;height:96px;margin:0 auto;border-radius:50%;border:2px solid var(--orange);display:flex;align-items:center;justify-content:center}
.why-item h3{font-weight:400;font-size:21px;margin-top:18px}
.why-item p{font-size:12px;line-height:19px;margin-top:10px;color:#ddd;padding:0 20px}

/* news */
.news-title{top:3258px}
.news-card{position:absolute;top:3345px;width:292px;height:382px;background:var(--white);box-shadow:0 4px 16px rgba(0,0,0,.1);overflow:hidden}
.news-img{width:292px;height:172px}
.news-body{padding:18px 22px}
.news-body h4{font-family:"Cinzel",serif;font-weight:400;font-size:16px;line-height:20px;color:var(--orange)}
.news-body p{font-size:12.5px;line-height:19px;color:var(--text);margin-top:10px}
.news-btn{width:122px;height:32px;font-size:11px;font-weight:500;margin-top:12px;color:var(--ink)}
.date-badge{position:absolute;background:var(--orange);color:var(--white);display:flex;align-items:center;gap:8px;padding:4px 18px 4px 10px;clip-path:polygon(0 0,100% 0,88% 100%,0 100%)}
.date-badge small{font-size:10px;line-height:10px;font-weight:500}
.date-badge b{font-size:22px;font-weight:500}

/* press */
.press{left:0;top:3811px;width:1200px;height:354px;background:var(--light)}
.press-cell{position:absolute;width:200px;height:90px;display:flex;align-items:center;justify-content:center;font-size:20px;font-weight:600;color:#1d2b4f;text-align:center;line-height:24px}
.press-cell.boxed{background:var(--white);box-shadow:0 3px 12px rgba(0,0,0,.08)}
.press-rule{position:absolute;background:#d4d4d4}

/* footer */
.site-footer{left:0;top:4165px;width:1200px;height:398px;background:var(--footer);color:#ddd}
.foot-head{position:absolute;top:4224px;font-size:19px;font-weight:600;color:var(--white)}
.foot-line{position:absolute;font-size:13px;line-height:18px;color:#ddd;display:flex;gap:12px;align-items:flex-start}
.foot-link{position:absolute;left:429px;font-size:13px;color:#ddd}
.soc{position:absolute;top:4417px;width:32px;height:32px;border-radius:50%;border:1.5px solid #ddd}
.field{position:absolute;border:1px solid #555;background:#1e1e1e;color:#999;font-size:13px;padding:8px 14px}
.send{position:absolute;left:626px;top:4424px;width:104px;height:34px;background:var(--orange);color:var(--white);font-size:14px;display:flex;align-items:center;justify-content:center}
.foot-rule{position:absolute;left:0;top:4493px;width:1200px;height:1px;background:#3a3a3a}
.foot-brand{position:absolute;left:133px;top:4508px;display:flex;align-items:center;gap:8px}
.foot-brand span{font-family:"Cinzel",serif;font-size:14px;color:var(--orange);line-height:16px;width:150px}
.copyright{position:absolute;right:117px;top:4520px;font-size:13px;color:#ccc}
</style>
</head>
<body>

<header class="site-header">
  <div class="brand">
    <div class="brand-name">Halvern Ridge Advisory LLC</div>
    <div class="brand-mark"></div>
  </div>
  <nav class="nav">
    <a class="active">Home</a><a>About Us</a><a>Our Experts</a><a>News &amp; Events</a><a>Careers</a><a>Contact Us</a>
  </nav>
  <div class="phone">
    <span class="phone-ic"><svg width="14" height="14" viewBox="0 0 24 24" fill="#fff"><path d="M6.6 10.8a15 15 0 0 0 6.6 6.6l2.2-2.2a1 1 0 0 1 1-.25 11.4 11.4 0 0 0 3.6.57 1 1 0 0 1 1 1V20a1 1 0 0 1-1 1A17 17 0 0 1 3 4a1 1 0 0 1 1-1h3.5a1 1 0 0 1 1 1c0 1.25.2 2.45.57 3.57a1 1 0 0 1-.25 1z"/></svg></span>
    555 010 2040
  </div>
</header>

<section class="hero">
  <div class="hero-art" role="img" aria-label="Glowing orange digital fingerprint over a circuit board with streams of binary light"></div>
  <div class="hero-curve"></div>
  <p class="abs hero-kicker serif">A Technology Consultant</p>
  <h1 class="abs hero-title serif">That Solves Real World<br>Business Problems</h1>
  <p class="abs hero-copy">Lorem Ipsum is simply dummy text of the printing and typesetting industry. Lorem Ipsum has been the industry's standard dummy text ever since</p>
  <a class="abs btn-solid hero-btn">Get In Touch <span class="circ-ic"><svg width="8" height="10" viewBox="0 0 8 10"><path d="M2 1l4 4-4 4" fill="none" stroke="#fff" stroke-width="1.8"/></svg></span></a>
  <div class="abs arrow-btn arrow-outline" style="left:1009px;top:299px"><svg width="12" height="16" viewBox="0 0 12 16"><path d="M9 2L3 8l6 6" fill="none" stroke="#fff" stroke-width="2"/></svg></div>
  <div class="abs arrow-btn arrow-fill" style="left:1069px;top:299px"><svg width="12" height="16" viewBox="0 0 12 16"><path d="M3 2l6 6-6 6" fill="none" stroke="#fff" stroke-width="2"/></svg></div>
</section>

<section>
  <div class="abs welcome-art" role="img" aria-label="Connected network of metallic and orange spheres around a glowing circuit chip"></div>
  <div class="abs welcome-node" role="img" aria-label="Orange circuit chip at the centre of the network"></div>
  <p class="abs kicker-dark serif">Welcome To</p>
  <h2 class="abs welcome-title serif">Halvern Ridge</h2>
  <p class="abs welcome-copy">Lorem Ipsum has been the industry's standard dummy text ever since the 1500s, when an unknown printer took a galley of type and scrambled it to make a type specimen book. It has survived not only five centuries, but also the leap into electronic typesetting, remaining essentially unchanged.</p>
  <a class="abs btn-outline welcome-btn">Learn More <span class="circ-ic"><svg width="8" height="10" viewBox="0 0 8 10"><path d="M2 1l4 4-4 4" fill="none" stroke="#f07c1b" stroke-width="1.8"/></svg></span></a>
</section>

<section class="abs services">
  <h2 class="abs section-title serif" style="top:60px">Our Services We Offer</h2>

  <div class="service-card" style="left:144px;top:182px">
    <svg viewBox="0 0 100 100" fill="none" stroke="#f07c1b" stroke-width="4"><circle cx="50" cy="48" r="36"/><path d="M33 48l12 12 22-24" stroke-linecap="round" stroke-linejoin="round"/></svg>
    <span class="label">Cyber Security</span>
  </div>
  <div class="service-card featured" style="left:464px;top:182px">
    <svg viewBox="0 0 100 100" fill="none" stroke="#fff" stroke-width="4"><circle cx="55" cy="44" r="18"/><path d="M68 57l20 20" stroke-linecap="round"/><circle cx="22" cy="58" r="6"/><circle cx="72" cy="16" r="5"/><path d="M28 55l12-6M66 20l-5 8"/></svg>
    <span class="label">Data Analytics</span>
  </div>
  <div class="service-card" style="left:783px;top:182px">
    <svg viewBox="0 0 100 100" fill="none" stroke="#f07c1b" stroke-width="4"><path d="M28 46a14 14 0 0 1 4-27 18 18 0 0 1 34 2 12 12 0 0 1 4 25z"/><path d="M50 46v22M50 68l-24 12M50 68l24 12M36 56h28"/><circle cx="22" cy="82" r="6"/><circle cx="78" cy="82" r="6"/><circle cx="50" cy="68" r="5"/></svg>
    <span class="label">Project Management</span>
  </div>
  <div class="service-card" style="left:292px;top:462px">
    <svg viewBox="0 0 100 100" fill="none" stroke="#f07c1b" stroke-width="4"><rect x="18" y="44" width="46" height="32" rx="8"/><circle cx="33" cy="60" r="4"/><circle cx="50" cy="60" r="4"/><path d="M12 54v12M70 54v12M41 44v-8"/><rect x="56" y="12" width="30" height="36" rx="3"/><path d="M63 22h16M63 30h16M63 38h10"/></svg>
    <span class="label">Risk Management</span>
  </div>
  <div class="service-card" style="left:612px;top:462px">
    <svg viewBox="0 0 100 100" fill="none" stroke="#f07c1b" stroke-width="4" stroke-linecap="round"><circle cx="50" cy="22" r="9"/><path d="M36 48a14 14 0 0 1 28 0"/><path d="M14 40v20l18 20h14v-14l-12-12M86 40v20L68 80H54V66l12-12"/></svg>
    <span class="label">It Consulting</span>
  </div>
</section>

<section>
  <svg class="abs dark-band" viewBox="0 0 1200 1015" preserveAspectRatio="none" role="img" aria-label="Dark night-blue digital backdrop with faint glowing data streams">
    <defs>
      <linearGradient id="nightGrad" x1="0" y1="0" x2="0" y2="1">
        <stop offset="0" stop-color="#03080c"/>
        <stop offset=".45" stop-color="#0a2230"/>
        <stop offset="1" stop-color="#040b10"/>
      </linearGradient>
    </defs>
    <polygon points="0,96 355,4 1200,150 1200,1015 0,1015" fill="url(#nightGrad)"/>
  </svg>

  <h2 class="abs experts-title serif">Our Experts</h2>
  <p class="abs experts-copy">Lorem Ipsum is simply dummy text of the printing and typesetting industry. Lorem Ipsum has been the industry's standard dummy text</p>
  <div class="abs arrow-sm" style="left:165px;top:2605px;border:2px solid var(--orange)"><svg width="10" height="12" viewBox="0 0 10 12"><path d="M7 1L2 6l5 5" fill="none" stroke="#f07c1b" stroke-width="1.8"/></svg></div>
  <div class="abs arrow-sm" style="left:211px;top:2605px;background:var(--orange)"><svg width="10" height="12" viewBox="0 0 10 12"><path d="M3 1l5 5-5 5" fill="none" stroke="#fff" stroke-width="1.8"/></svg></div>

  <div class="expert-card" style="left:572px">
    <div class="expert-photo" role="img" aria-label="Portrait of the managing principal"></div>
    <div class="expert-name">ExpertsName</div>
    <div class="expert-role">Managing Principal</div>
    <div class="social-dot"></div>
  </div>
  <div class="expert-card" style="left:789px">
    <div class="expert-photo" role="img" aria-label="Portrait of the management consultant"></div>
    <div class="expert-name">ExpertsName</div>
    <div class="expert-role">Management<br>Consultant</div>
    <div class="social-dot"></div>
  </div>

  <h2 class="abs section-title serif why-title">Why Choose Us</h2>
  <div class="why-item" style="left:312px">
    <div class="why-ic"><svg width="50" height="50" viewBox="0 0 50 50" fill="none" stroke="#f07c1b" stroke-width="3" stroke-linecap="round"><circle cx="29" cy="20" r="12"/><path d="M20 29L8 41"/><circle cx="29" cy="20" r="4" fill="#f07c1b"/></svg></div>
    <h3>Professionalism</h3>
    <p>Use our body field scanner, at home to uncover why yhou feelthe way you do</p>
  </div>
  <div class="why-item" style="left:606px">
    <div class="why-ic"><svg width="50" height="50" viewBox="0 0 50 50" fill="none" stroke="#f07c1b" stroke-width="3" stroke-linecap="round" stroke-linejoin="round"><circle cx="24" cy="26" r="16"/><path d="M16 26l7 7 18-20"/></svg></div>
    <h3>Better Results</h3>
    <p>Use our body field scanner, at home to uncover why yhou feelthe way you do</p>
  </div>
  <div class="why-item" style="left:886px">
    <div class="why-ic"><svg width="50" height="50" viewBox="0 0 50 50" fill="none" stroke="#f07c1b" stroke-width="3" stroke-linecap="round"><circle cx="12" cy="12" r="4"/><circle cx="38" cy="25" r="4"/><circle cx="12" cy="38" r="4"/><path d="M16 12h12a6 6 0 0 1 6 6v3M34 25H16a4 4 0 0 0-4 4v5M16 38h16"/></svg></div>
    <h3>Quality Work</h3>
    <p>Use our body field scanner, at home to uncover why yhou feelthe way you do</p>
  </div>
</section>

<section>
  <h2 class="abs section-title serif news-title">Latest News</h2>

  <article class="news-card" style="left:140px">
    <div class="news-img" role="img" aria-label="Hand touching a glowing digital data interface" style="background:linear-gradient(135deg,#0a2a44,#1f6a9a 55%,#0b1d2e)"></div>
    <div class="date-badge" style="left:0;top:20px"><small>JAN<br>2020</small><b>18</b></div>
    <div class="news-body">
      <h4>Industry's Standard<br>Dummy Text Ever</h4>
      <p>Lorem Ipsum is simply dummy text of the printing &amp; typesetting industry. Lorem Ipsum</p>
      <a class="btn-outline news-btn">LEARN MORE</a>
    </div>
  </article>

  <article class="news-card" style="left:457px">
    <div class="news-body" style="padding-top:18px;height:210px">
      <h4>Industry's Standard<br>Dummy Text Ever</h4>
      <p>Lorem Ipsum is simply dummy text of the printing &amp; typesetting industry. Lorem Ipsum</p>
      <a class="btn-outline news-btn">LEARN MORE</a>
    </div>
    <div class="news-img" role="img" aria-label="Blue digital globe with network lines" style="background:radial-gradient(circle at 55% 40%,#2f7fb4,#0d3352 60%,#061826)"></div>
    <div class="date-badge" style="left:0;top:320px"><small>JAN<br>2020</small><b>18</b></div>
  </article>

  <article class="news-card" style="left:773px">
    <div class="news-img" role="img" aria-label="Hands typing on a laptop with a glowing digital overlay" style="background:linear-gradient(135deg,#cfd6dc,#7c8a97 55%,#2d3b48)"></div>
    <div class="date-badge" style="left:0;top:20px"><small>JAN<br>2020</small><b>18</b></div>
    <div class="news-body">
      <h4>Industry's Standard<br>Dummy Text Ever</h4>
      <p>Lorem Ipsum is simply dummy text of the printing &amp; typesetting industry. Lorem Ipsum</p>
      <a class="btn-outline news-btn">LEARN MORE</a>
    </div>
  </article>
</section>

<section class="abs press">
  <div class="press-rule" style="left:150px;top:175px;width:890px;height:1px"></div>
  <div class="press-rule" style="left:373px;top:190px;width:1px;height:120px"></div>
  <div class="press-rule" style="left:603px;top:190px;width:1px;height:120px"></div>
  <div class="press-rule" style="left:828px;top:190px;width:1px;height:120px"></div>

  <div class="press-cell boxed" style="left:190px;top:74px;width:152px;height:70px">Northfield Review</div>
  <div class="press-cell boxed" style="left:385px;top:62px;width:212px;height:100px">Ledger Journal</div>
  <div class="press-cell" style="left:630px;top:74px;width:180px;height:70px">Venture Weekly</div>
  <div class="press-cell boxed" style="left:845px;top:74px;width:190px;height:70px">Capital Week</div>

  <div class="press-cell" style="left:160px;top:195px;width:200px;height:80px">Nation Daily</div>
  <div class="press-cell boxed" style="left:390px;top:195px;width:196px;height:80px">Newsline</div>
  <div class="press-cell" style="left:650px;top:190px;width:140px;height:90px">Ledger Journal</div>
  <div class="press-cell boxed" style="left:875px;top:195px;width:150px;height:80px">Northfield Review</div>
</section>

<footer class="abs site-footer"></footer>
<div class="foot-head" style="left:140px">CONTACT US</div>
<div class="foot-line" style="left:140px;top:4262px">
  <svg width="14" height="18" viewBox="0 0 14 18"><path d="M7 1a6 6 0 0 1 6 6c0 4-6 10-6 10S1 11 1 7a6 6 0 0 1 6-6z" fill="#fff"/><circle cx="7" cy="7" r="2.2" fill="#151515"/></svg>
  <span>48 Alder Court #5<br>Fairview 20140</span>
</div>
<div class="foot-line" style="left:140px;top:4320px;color:var(--orange)">
  <svg width="16" height="16" viewBox="0 0 24 24" fill="#fff"><path d="M6.6 10.8a15 15 0 0 0 6.6 6.6l2.2-2.2a1 1 0 0 1 1-.25 11.4 11.4 0 0 0 3.6.57 1 1 0 0 1 1 1V20a1 1 0 0 1-1 1A17 17 0 0 1 3 4a1 1 0 0 1 1-1h3.5a1 1 0 0 1 1 1c0 1.25.2 2.45.57 3.57a1 1 0 0 1-.25 1z"/></svg>
  <span>(00) 555 0100 200</span>
</div>
<div class="foot-line" style="left:140px;top:4362px">
  <svg width="16" height="14" viewBox="0 0 16 14"><rect x="1" y="2" width="14" height="10" fill="none" stroke="#fff" stroke-width="1.5"/><path d="M1 2l7 6 7-6" fill="none" stroke="#fff" stroke-width="1.5"/></svg>
  <span>office@halvernridge.example</span>
</div>
<div class="soc" style="left:133px"></div>
<div class="soc" style="left:172px"></div>
<div class="soc" style="left:211px"></div>
<div class="soc" style="left:250px"></div>

<div class="foot-head" style="left:429px">COMPANY</div>
<div class="foot-link" style="top:4262px">Home</div>
<div class="foot-link" style="top:4292px">About Us</div>
<div class="foot-link" style="top:4322px">Our Experts</div>
<div class="foot-link" style="top:4352px">News &amp; Events</div>
<div class="foot-link" style="top:4382px">Careers</div>
<div class="foot-link" style="top:4412px">Contact Us</div>

<div class="field" style="left:626px;top:4229px;width:220px;height:35px">Name</div>
<div class="field" style="left:855px;top:4229px;width:212px;height:35px">Email</div>
<div class="field" style="left:626px;top:4275px;width:441px;height:34px">Subject</div>
<div class="field" style="left:626px;top:4319px;width:441px;height:94px">Message</div>
<div class="send">Send</div>

<div class="foot-rule"></div>
<div class="foot-brand"><span>Halvern Ridge Advisory LLC</span></div>
<div class="copyright">© 2020 Halvern Ridge. All Rights are Reserved.</div>

</body>
</html>
```